Quarvex Power Point Template - Institutional Presentation

Develop a comprehensive template for a corporate presentation power point.

The presentation will be aimed to institutional investors.

Style to be modern and contemporary. Use of icons and images welcome but not to much.

It would be great if you could develop the layout/style for the content in the following slides:

- Cover
- Section title
- Slide with title and bullet points on one side and two text boxes on the other side
- Slide with line chart and pie chart
- Slide with table

Should we like the slides above we will then develop the rest of the template.

We may then need to have a dark-background version - but this will be invoiced separately.

Target Market(s)

Corporate institutional investors

Industry/Entity Type

Finance

Font styles to use
Serif
Sans Serif

Colors
3176b5
0255a3
cee9f5
86cae7
33a6d7
0792cd
33b8a4
00a990
86cfc6

Requirements
Must have
• Mostly white background with minimal objects
Nice to have
• Use of photos, but not to much.

```html
<!DOCTYPE html>
<html lang="en">
<head>
<meta charset="utf-8">
<title>Quarvex – Institutional Investors Proposal Template</title>
<link href="https://fonts.googleapis.com/css2?family=Montserrat:wght@500;600;700&family=Raleway:wght@400;500&family=Didact+Gothic&display=swap" rel="stylesheet">
<style>
:root{
  --blue:#3176b5;
  --royal:#0255a3;
  --ice:#cee9f5;
  --sky:#86cae7;
  --cyan:#33a6d7;
  --ocean:#0792cd;
  --teal:#33b8a4;
  --jade:#00a990;
  --mint:#86cfc6;
  --navy:#1b2a52;
  --ink:#444;
  --muted:#8a8a8a;
  --grid:#e2e2e2;
}
*{box-sizing:border-box;margin:0;padding:0}
html,body{width:1200px;height:1200px;overflow:hidden;background:#fff}
body{position:relative;font-family:"Didact Gothic",sans-serif;color:var(--ink)}
.slide{position:absolute;width:540px;height:303px;background:#fff;overflow:hidden;box-shadow:0 1px 3px rgba(0,0,0,.18)}
.s1{left:38px;top:61px}.s2{left:622px;top:61px}
.s3{left:38px;top:444px}.s4{left:622px;top:444px}
.s5{left:38px;top:837px}.s6{left:622px;top:837px}
.abs{position:absolute}
.photo{position:absolute;inset:0}
.brand-badge{position:absolute;background:var(--navy);color:#fff;font-family:"Montserrat",sans-serif;font-weight:600;display:flex;align-items:center;justify-content:center;letter-spacing:.14em}
/* cover */
.s1 .photo{background:linear-gradient(100deg,#d9540e 0%,#ec7a12 30%,#b98a6b 55%,#b9bdc6 75%,#6a4a34 100%)}
.cover-block-top{left:31px;top:0;width:193px;height:122px;background:var(--blue)}
.cover-block-bottom{left:31px;top:246px;width:193px;height:57px;background:var(--jade)}
.s1 .brand-badge{left:74px;top:146px;width:107px;height:27px;font-size:12px}
.cover-title{position:absolute;left:0;width:256px;top:186px;text-align:center;color:#fff;font-family:"Montserrat",sans-serif;font-weight:700;font-size:16px;line-height:1.2}
.cover-sub{position:absolute;left:0;width:256px;top:211px;text-align:center;color:#fff;font-family:"Montserrat",sans-serif;font-weight:700;font-size:12.5px}
/* section */
.s2 .photo{background:linear-gradient(180deg,#0f1a22 0%,#23313a 40%,#4a3d2c 70%,#2a2c30 92%,#5a6672 100%)}
.section-block{left:31px;top:0;width:193px;height:93px;background:var(--blue)}
.section-rule{left:31px;top:99px;width:193px;height:7px;background:var(--mint)}
.section-title{left:70px;top:124px;color:#fff;font-family:"Montserrat",sans-serif;font-weight:600;font-size:19px}
/* content header */
.head-bar{left:18px;top:0;width:4px;height:39px;background:var(--blue)}
.head-title{left:36px;top:11px;font-family:"Raleway",sans-serif;font-size:14.5px;color:var(--teal);letter-spacing:.02em}
.content .brand-badge{left:440px;top:12px;width:78px;height:19px;font-size:9.5px}
.footer-note{left:18px;top:289px;font-size:4.5px;color:var(--muted)}
.page-no{left:519px;top:286px;font-size:6px;color:var(--muted)}
/* bullets */
.bullets{left:19px;top:55px;list-style:none;font-size:7px;line-height:18px;color:var(--ink)}
.bullets li::before{content:"•";margin-right:6px}
.text-col{left:235px;top:57px;width:275px;font-size:7.2px;line-height:13.5px}
.text-col p+p{margin-top:14px}
/* features */
.feature{position:absolute;top:72px;width:132px;text-align:center}
.feature svg{display:block;margin:0 auto}
.feature h3{margin-top:22px;font-family:"Montserrat",sans-serif;font-weight:600;font-size:8.5px}
.feature p{margin-top:3px;font-size:7px;line-height:13.6px;color:var(--ink)}
.f1{left:32px}.f1 h3{color:var(--ocean)}
.f2{left:196px}.f2 h3{color:var(--jade)}
.f3{left:359px}.f3 h3{color:var(--cyan)}
/* table */
.stake-table{position:absolute;left:21px;top:61px;width:475px;border-collapse:collapse;font-size:5.8px;table-layout:fixed}
.stake-table th{background:var(--teal);color:#fff;font-family:"Montserrat",sans-serif;font-weight:700;font-size:5.5px;height:29px;padding:0 3px;border-right:1px solid #fff;line-height:1.25}
.stake-table td{background:var(--ice);color:#555;padding:0 7px;border-right:1px solid #fff;border-top:1px solid #fff;line-height:11px;vertical-align:middle}
/* charts */
.chart-title{font-family:"Raleway",sans-serif;font-size:10px;color:#555}
.axis{font-size:6.5px;fill:#666;font-family:"Didact Gothic",sans-serif}
</style>
</head>
<body>

<section class="slide s1">
  <div class="photo" role="img" aria-label="Photo of a person writing in a notebook beside a laptop on a wooden desk, orange wall behind"></div>
  <div class="abs cover-block-top"></div>
  <div class="abs cover-block-bottom"></div>
  <div class="brand-badge">QUARVEX</div>
  <div class="cover-title">INSTITUTIONAL INVESTORS</div>
  <div class="cover-sub">PROPOSAL</div>
</section>

<section class="slide s2">
  <div class="photo" role="img" aria-label="Photo of a lit office building entrance at dusk with people walking past"></div>
  <div class="abs section-block"></div>
  <div class="abs section-rule"></div>
  <div class="abs section-title">TITLE SLIDE</div>
</section>

<section class="slide s3 content">
  <div class="abs head-bar"></div>
  <div class="abs head-title">LOREM IPSUM DOLOR</div>
  <div class="brand-badge">QUARVEX</div>
  <ul class="abs bullets">
    <li>Lorem ipsum dolor sit amet</li>
    <li>consectetur adipiscing elit</li>
    <li>Integer sodales orci ve</li>
    <li>faucibus dignissim</li>
    <li>Aenean est odio</li>
    <li>blandit ut dolor in</li>
    <li>pellentesque fermentum sapien</li>
    <li>Cras scelerisque metus ut</li>
    <li>vulputate suscipit</li>
    <li>In a mauris metus</li>
    <li>Integer ipsum urna</li>
    <li>semper a risus convallis</li>
  </ul>
  <div class="abs text-col">
    <p>rhoncus, ante ligula rutrum sapien, at euismod libero leo id quam. Sed consectetur quis felis rhoncus sagittis. Sed scelerisque ex dolor, at egestas enim tempor in. Aenean sit amet urna semper, suscipit nulla nec, auctor nulla.</p>
    <p>Mauris convallis justo ullamcorper, posuere dolor eget, sollicitudin dui. Vestibulum feugiat, enim at pretium lobortis, libero lectus condimentum nunc, eget condimentum nisi augue vitae ante.</p>
    <p>Sed et dui a neque dapibus eleifend at et velit. Vivamus interdum fringilla commodo. Vivamus ac vulputate lectus. Duis commodo enim id commodo tincidunt. Nunc lorem neque, posuere vitae semper ac, venenatis convallis risus. Phasellus auctor nunc sed elit viverra vehicula. Praesent tellus erat, maximus ac eleifend sed, scelerisque fermentum metus. Praesent at quam at tellus faucibus vestibulum eget ut ex. Nunc tincidunt maximus ante ut dictum. Ut porta dui a ex iaculis, eget faucibus mauris viverra.</p>
  </div>
  <div class="abs footer-note">© Quarvex 2017 - All Rights Reserved</div>
  <div class="abs page-no">3</div>
</section>

<section class="slide s4 content">
  <div class="abs head-bar"></div>
  <div class="abs head-title">LOREM IPSUM DOLOR</div>
  <div class="brand-badge">QUARVEX</div>

  <div class="feature f1">
    <svg width="82" height="68" viewBox="0 0 82 68">
      <g fill="var(--jade)">
        <rect x="1" y="2" width="52" height="10" rx="3"/>
        <rect x="1" y="15" width="44" height="10" rx="3"/>
        <rect x="1" y="28" width="40" height="10" rx="3"/>
        <rect x="1" y="41" width="40" height="10" rx="3"/>
        <rect x="1" y="54" width="44" height="10" rx="3"/>
      </g>
      <circle cx="55" cy="37" r="28" fill="#fff"/>
      <circle cx="55" cy="37" r="25" fill="var(--jade)"/>
      <circle cx="55" cy="37" r="19" fill="none" stroke="#fff" stroke-width="2.5"/>
      <text x="55" y="47" text-anchor="middle" fill="#fff" font-family="Montserrat,sans-serif" font-weight="700" font-size="28">$</text>
    </svg>
    <h3>Rhoncus ante ligula</h3>
    <p>rutrum sapien, at euismod libero leo id quam. Sed consectetur quis felis rhoncus sagittis. Sed scelerisque ex dolor, at egestas enim tempor in. Aenean sit amet urna semper, suscipit nulla nec, auctor nulla.</p>
  </div>

  <div class="feature f2">
    <svg width="78" height="68" viewBox="0 0 78 68">
      <g fill="var(--royal)">
        <rect x="2" y="2" width="20" height="64" rx="2"/>
        <rect x="26" y="2" width="20" height="64" rx="2"/>
        <rect x="50" y="2" width="20" height="64" rx="2" transform="rotate(-8 60 66)"/>
      </g>
      <g fill="none" stroke="#fff" stroke-width="2">
        <path d="M7 12h10M7 17h10M7 22h10M31 12h10M31 17h10M31 22h10"/>
        <circle cx="12" cy="50" r="4.5"/><circle cx="36" cy="50" r="4.5"/>
        <g transform="rotate(-8 60 66)"><path d="M55 12h10M55 17h10M55 22h10"/><circle cx="60" cy="50" r="4.5"/></g>
      </g>
    </svg>
    <h3>Rhoncus ante ligula</h3>
    <p>rutrum sapien, at euismod libero leo id quam. Sed consectetur quis felis rhoncus sagittis. Sed scelerisque ex dolor, at egestas enim tempor in. Aenean sit amet urna semper, suscipit nulla nec, auctor nulla.</p>
  </div>

  <div class="feature f3">
    <svg width="56" height="68" viewBox="0 0 56 68">
      <rect x="2" y="6" width="52" height="60" rx="3" fill="var(--mint)"/>
      <rect x="7" y="12" width="42" height="49" fill="#fff"/>
      <rect x="17" y="1" width="22" height="10" rx="2" fill="var(--mint)" stroke="#fff" stroke-width="1.5"/>
      <path d="M13 22h30M13 29h30M13 36h30M13 43h30M13 50h30" stroke="var(--mint)" stroke-width="2.5"/>
    </svg>
    <h3>Rhoncus ante ligula</h3>
    <p>rutrum sapien, at euismod libero leo id quam. Sed consectetur quis felis rhoncus sagittis. Sed scelerisque ex dolor, at egestas enim tempor in. Aenean sit amet urna semper, suscipit nulla nec, auctor nulla.</p>
  </div>

  <div class="abs footer-note">© Quarvex 2017 - All Rights Reserved</div>
  <div class="abs page-no">4</div>
</section>

<section class="slide s5 content">
  <div class="abs head-bar"></div>
  <div class="abs head-title">LOREM IPSUM DOLOR</div>
  <div class="brand-badge">QUARVEX</div>
  <table class="stake-table">
    <colgroup><col style="width:70px"><col style="width:76px"><col style="width:75px"><col style="width:85px"><col style="width:72px"><col style="width:97px"></colgroup>
    <thead>
      <tr><th>TARGET STAKEHOLDER AUDIENCE</th><th>DECISION MAKERS</th><th>PARTNERS FOR REACHING THEM</th><th>INTERESTED BODIES AND INDIVIDUALS</th><th>OTHER STAFF DEPENDENCIES</th><th>CHANNELS FOR REACHING THEM</th></tr>
    </thead>
    <tbody>
      <tr style="height:38px"><td>Regulators</td><td>Committees<br>Oversight Board</td><td>Lobbyists</td><td>Industry influencers</td><td>Strategy/ ExCo<br>Regulatory Policy</td><td>Direct<br>Website<br>Media</td></tr>
      <tr style="height:34px"><td>Public Policy</td><td>MPs<br>Cross party committees</td><td>Think Tanks<br>Lobbyists</td><td>Industry influencers</td><td>Strategy/ ExCo<br>Public Policy</td><td>Direct<br>Media</td></tr>
      <tr style="height:34px"><td>Employees</td><td>Individuals<br>Union bosses</td><td>Employee Groups<br>Unions</td><td>Unions</td><td>Strategy/ ExCo<br>HR</td><td>Direct<br>Intranet</td></tr>
      <tr style="height:38px"><td>Community</td><td>Individuals</td><td>Local authorities<br>Outreach programmes</td><td>Local Government</td><td>CSR Marketing</td><td>Website<br>Media</td></tr>
      <tr style="height:33px"><td>Suppliers</td><td>Sales/ product teams</td><td></td><td>Regulators<br>Politicians</td><td>CSR<br>Procurement</td><td>Direct<br>Website<br>Media</td></tr>
    </tbody>
  </table>
  <div class="abs footer-note">© Quarvex 2017 - All Rights Reserved</div>
  <div class="abs page-no">5</div>
</section>

<section class="slide s6 content">
  <div class="abs head-bar"></div>
  <div class="abs head-title">LOREM IPSUM DOLOR</div>
  <div class="brand-badge">QUARVEX</div>
  <svg class="abs" style="left:0;top:0" width="540" height="303" viewBox="0 0 540 303">
    <text x="150" y="74" text-anchor="middle" class="chart-title">Chart Title</text>
    <g stroke="var(--grid)" stroke-width=".6">
      <path d="M27 84H278M27 110.2H278M27 136.4H278M27 162.6H278M27 188.8H278M27 215H278"/>
      <path d="M27 241H278" stroke="#bbb"/>
    </g>
    <g class="axis" text-anchor="end">
      <text x="21" y="86">6</text><text x="21" y="112">5</text><text x="21" y="138.5">4</text>
      <text x="21" y="164.5">3</text><text x="21" y="191">2</text><text x="21" y="217">1</text><text x="21" y="243">0</text>
    </g>
    <g class="axis" text-anchor="middle">
      <text x="59" y="255">Category 1</text><text x="122" y="255">Category 2</text>
      <text x="185" y="255">Category 3</text><text x="248" y="255">Category 4</text>
    </g>
    <g fill="none" stroke-width="1.2">
      <polyline points="59,188.6 122,188.6 185,162.4 248,110" stroke="var(--sky)"/>
      <polyline points="59,178.1 122,125.7 185,193.8 248,167.6" stroke="var(--royal)"/>
      <polyline points="59,128.3 122,175.5 185,149.3 248,123.1" stroke="var(--jade)"/>
    </g>
    <g class="axis">
      <path d="M91 266.5h12" stroke="var(--jade)" stroke-width="1.2"/><text x="103" y="269">Series 1</text>
      <path d="M133 266.5h12" stroke="var(--royal)" stroke-width="1.2"/><text x="145" y="269">Series 2</text>
      <path d="M176 266.5h12" stroke="var(--sky)" stroke-width="1.2"/><text x="188" y="269">Series 3</text>
    </g>

    <text x="402" y="78" text-anchor="middle" class="chart-title">Series 1</text>
    <g stroke="#fff" stroke-width="1">
      <path d="M402 170L402 88A82 82 0 0 1 483.2 181.4Z" fill="var(--ocean)"/>
      <path d="M402 170L483.2 181.4A82 82 0 0 1 419.1 250.2Z" fill="var(--mint)"/>
      <path d="M402 170L419.1 250.2A82 82 0 0 1 329.6 208.5Z" fill="var(--sky)"/>
      <path d="M402 170L329.6 208.5A82 82 0 0 1 402 88Z" fill="var(--jade)"/>
    </g>
    <g class="axis">
      <rect x="306" y="262.5" width="3" height="3" fill="var(--ocean)"/><text x="311" y="266">Category 1</text>
      <rect x="357" y="262.5" width="3" height="3" fill="var(--mint)"/><text x="362" y="266">Category 2</text>
      <rect x="408" y="262.5" width="3" height="3" fill="var(--sky)"/><text x="413" y="266">Category 3</text>
      <rect x="459" y="262.5" width="3" height="3" fill="var(--jade)"/><text x="464" y="266">Category 4</text>
    </g>
  </svg>
  <div class="abs footer-note">© Quarvex 2017 - All Rights Reserved</div>
  <div class="abs page-no">6</div>
</section>

</body>
</html>
```